Redo of existing website www.brontivel.com

I would like it to look like the newer style website, with large images, less text. clean and modern looking. The new design should focus on call to action. ultimately that's what were looking for.Some features I would like to see we try to do good job of keeping up with our blog, and it is a good source of recent pictures of our work. I like four visitors to get the few pieces they're doing with a national brand or franchise pray. I like to stay far from the idea of a local one-man band with magnetic signs on his truck.
I think that clean beautiful images have the biggest impact. In my opinion most people don't read more than a couple lines of text. The text is more for search engines.
we are currently in the process of revising our logo as well, I will upload those files when I get them.
Please feel free to use content and images from our current website www.brontivel.com. we can purchase professional stock images if needed.
1. large call to action with easy contact form.
2. Blog roll on front page to showcase our recent work.
2. All social connect buttons.
Check out our reviews on zindexa!
My current websites
Www.brontivel.com
https://plus.vorplink.com/593028416627304918735/about
www.chatterbook.com/brontivel
http://www.skimblr.com/blog/curbmarauder
https://chirpfeed.com/Brontivel
websites I like the way they look.
http://postwren.com/
http://www.vendlio.com/
http://www.corvanblacktop.com/
http://www.tarwayguild.org/
http://groundsurfacecrafts.com/
Updates
Hello all,
I have just uploaded some images of our company mascot "Curb Marauder" and our new logo.
Project Deadline Extended
Reason: Death in family. Finally back to work.
Target Market(s)
We have 2 main groups of customers commercial and residential.
Commercial customers are Property owners and managers, operators of multi location business, restaurant, supermarket, banks, and are best source for repeat business
for Residential customers we provide driveway repair and driveway paving services.
for residential customers I would like to encourge the submission or pictures with the inquiry for a quick quote. Residential customers are typically a one time job but are a good source of referrals
I like how this website separates residential and commercial
http://www.glintcoatdirect.com
Industry/Entity Type
Call
Look and feel
Each slider illustrates characteristics of the customer's brand and the style your logo design should communicate.

```html
<!DOCTYPE html>
<html lang="en">
<head>
<meta charset="utf-8">
<title>Brontivel — Asphalt Paving</title>
<link href="https://fonts.googleapis.com/css2?family=Open+Sans:ital,wght@0,400;0,600;0,700;1,400;1,600&display=swap" rel="stylesheet">
<style>
:root{
  --green:#2fd52f;
  --green-dark:#1f8f1f;
  --panel:#262626;
  --panel-2:#2e2e2e;
  --text:#e6e6e6;
  --muted:#9a9a9a;
  --white:#ffffff;
}
*{box-sizing:border-box;margin:0;padding:0}
html,body{width:799px;height:1200px;overflow:hidden}
body{position:relative;background:radial-gradient(ellipse at 50% 40%,#2b2b2b,#151515 80%);font-family:"Open Sans",sans-serif;color:var(--text)}
.abs{position:absolute}
.header{left:0;top:0;width:799px;height:118px;background:linear-gradient(#3a3a3a,#262626)}
.brand{left:36px;top:24px;display:flex;align-items:center;gap:10px}
.brand-mark{width:22px;height:22px;background:var(--green-dark)}
.brand-name{font-weight:700;font-size:26px;color:var(--white);line-height:1}
.call{right:54px;top:17px;font-size:13.5px;font-weight:600;color:var(--white)}
.social{right:54px;top:52px;display:flex;gap:7px}
.social span{width:24px;height:24px;border:2px solid #ddd;border-radius:50%;font-size:9px;font-weight:700;display:flex;align-items:center;justify-content:center;color:#ddd}
.social span:first-child{border-color:var(--green);color:var(--green)}
.nav{left:55px;top:98px;width:700px;height:36px;background:linear-gradient(#2c3a3e,#1d2628);border-bottom:3px solid #111;display:flex;z-index:3;box-shadow:0 2px 4px rgba(0,0,0,.6)}
.nav a{color:#e8e8e8;text-decoration:none;font-size:11.5px;padding:0 11px;display:flex;align-items:center;border-right:1px solid #3f4b4e}
.nav a.active{background:var(--green-dark);color:var(--white)}
.nav a.last{border:0}
.nav .search{margin-left:auto;width:32px;background:var(--green-dark);justify-content:center;padding:0;border:0}
.slider{left:0;top:118px;width:799px;height:352px;background:linear-gradient(#bfd4e6 0%,#dfe3e1 25%,#9fb59d 45%,#bdbab4 62%,#8a8a86 100%)}
.arrow{top:311px;width:29px;height:29px;border-radius:50%;background:#111;display:flex;align-items:center;justify-content:center}
.caption{left:152px;top:347px;width:495px;height:79px;background:rgba(40,40,40,.85);border-left:3px solid var(--green);border-right:3px solid var(--green);padding:8px 0 0 18px;font-style:italic;font-size:20.5px;line-height:30px;color:var(--white)}
.services{left:44px;top:470px;width:710px;height:176px;background:#151515;display:flex;gap:10px;padding:10px 11px}
.card{width:165px}
.card .photo{height:126px;background:linear-gradient(#7aa0c0,#8c8a80 55%,#4a4a48)}
.card .photo.alt{background:linear-gradient(#a09b90,#6a6a66 60%,#303030)}
.card .photo.water{background:linear-gradient(#6a8aa8,#3d5a74 50%,#2b3f4f)}
.card .label{height:35px;padding:8px 15px;font-size:14px;color:#7a7a7a;background:#1d1d1d;border-bottom:1px solid var(--green-dark);white-space:nowrap;overflow:hidden}
.card.active .label{background:var(--green-dark);color:var(--white);font-weight:600}
.welcome-title{left:55px;top:658px;font-size:16px;font-weight:700;color:var(--green)}
.welcome-text{left:54px;top:686px;width:700px;font-size:9.6px;line-height:14.6px;color:#f0f0f0;font-weight:400}
.blog{left:55px;top:762px;width:424px;height:212px;background:var(--panel)}
.blog h2{font-size:16px;color:var(--green);padding:6px 15px;height:30px}
.post{height:61px;display:flex;padding:6px 8px;gap:10px}
.post.active{background:var(--panel-2)}
.date{width:42px;height:42px;border-radius:50%;background:#1a1a1a;margin-top:8px;text-align:center;line-height:1;flex:none}
.date b{display:block;font-style:italic;font-size:14px;color:var(--green);padding-top:8px}
.date i{font-size:8px;color:var(--muted)}
.post h3{font-size:11.5px;font-weight:400;color:#eee}
.post.active h3{color:var(--green)}
.post .time{font-size:9px;font-style:italic;color:var(--muted);margin:1px 0 3px}
.post p{font-size:9.2px;color:#cfcfcf}
.video-title{left:525px;top:759px;font-size:16px;font-weight:700;color:var(--green)}
.video{left:526px;top:789px;width:228px;height:185px;background:linear-gradient(135deg,#3a3f38,#2a2e2a 50%,#3b3f3a);border:1px solid #555;display:flex;align-items:center;justify-content:center}
.play{width:30px;height:30px;border-radius:50%;border:2px solid #fff;background:rgba(0,0,0,.4);display:flex;align-items:center;justify-content:center}
.footer h4{font-size:14.5px;font-weight:600;color:var(--white)}
.footer ul{list-style:none;margin-top:8px}
.footer li{font-size:9px;color:#ddd;line-height:16.2px}
.footer li.current{color:var(--green)}
.field{width:159px;height:25px;background:#9a9a9a;border:1px solid #bbb;font-size:9px;color:#333;padding:6px 7px}
.send{width:57px;height:24px;background:#2fb82f;color:var(--white);font-size:12px;font-weight:600;display:flex;align-items:center;justify-content:center}
.cards{display:flex;gap:7px;margin-top:10px}
.cards span{width:29px;height:18px;background:#e9e9e9;color:#333;font-size:5px;font-weight:700;display:flex;align-items:center;justify-content:center;overflow:hidden}
.badge{width:62px;height:56px;border-radius:50%;background:#d8d8d8;border:3px solid #6a6a6a}
.copyright{left:0;top:1162px;width:799px;height:38px;background:#0f0f0f;font-size:9.5px;color:#ddd;padding:11px 34px}
</style>
</head>
<body>
<header class="abs header">
  <div class="abs brand"><span class="brand-mark"></span><span class="brand-name">BRONTIVEL</span></div>
  <div class="abs call">Call Free: (555) 418-2270</div>
  <div class="abs social"><span>Cb</span><span>Cf</span><span>Sk</span><span>Vp</span><span>Lw</span></div>
</header>
<nav class="abs nav">
  <a class="active">HOME</a><a>COMMERCIAL</a><a>RESIDENTIAL</a><a>ABOUT US</a><a>FREE ESTIMATE</a><a>TESTIMONIALS</a><a class="last">BLOG</a>
  <a class="search"><svg width="13" height="13" viewBox="0 0 13 13"><circle cx="5.5" cy="5.5" r="4" fill="none" stroke="#fff" stroke-width="2"/><line x1="8.5" y1="8.5" x2="12" y2="12" stroke="#fff" stroke-width="2"/></svg></a>
</nav>
<section class="abs slider" role="img" aria-label="Paving crew sealing a shopping center parking lot"></section>
<div class="abs arrow" style="left:34px"><svg width="12" height="12" viewBox="0 0 12 12"><path d="M8 1 3 6l5 5" fill="none" stroke="#fff" stroke-width="2"/></svg></div>
<div class="abs arrow" style="left:736px"><svg width="12" height="12" viewBox="0 0 12 12"><path d="M4 1l5 5-5 5" fill="none" stroke="#fff" stroke-width="2"/></svg></div>
<div class="abs caption">Brontivel Provides custom hihg-quality deiverway<br>Paying to fit your beed and budget</div>
<section class="abs services">
  <div class="card active"><div class="photo" role="img" aria-label="Workers repairing asphalt"></div><div class="label">Asphalt Repairs</div></div>
  <div class="card"><div class="photo" role="img" aria-label="Workers repairing asphalt"></div><div class="label">Asphalt Repairs</div></div>
  <div class="card"><div class="photo alt" role="img" aria-label="Skid loader and worker spreading asphalt"></div><div class="label">Commercial Asphalti</div></div>
  <div class="card"><div class="photo water" role="img" aria-label="Worker sealcoating a driveway"></div><div class="label">Driveway</div></div>
</section>
<h1 class="abs welcome-title">Welcome to our Website</h1>
<p class="abs welcome-text">Brontivel specializes in pothole repairs, quality residential driveways, driveway repairs,&nbsp; commercial asphalt repair and parking lot paving services in NY areas Commercial Parking Lot Paving, Parking Lot Repair, Commercial Sealing, Parking Lot Resurfacing, Parking Lot Lines, Commercial Paving,&nbsp; Asphalt Repair, Blacktop Paving Rochester, NY, Syracuse, NY &amp;amp; Buffalo Commercial Parking Lot Paving &amp;amp; Parking Lot Repair&nbsp; Commercial Paving, Repair, Sealing &amp;amp; Resurfacing&nbsp; Rochester, Syracuse &amp;amp; Buffalo.</p>
<section class="abs blog">
  <h2>Blog</h2>
  <div class="post active"><div class="date"><b>25</b><i>Dec</i></div><div><h3>Lorem ipsum dolor sit amet,</h3><div class="time">◷ 11:00 PM to 7 : 00 pm</div><p>Lorem consectetur adipiscing elit.Lorem consectetur adipiscing elit.Lorem const.</p></div></div>
  <div class="post"><div class="date"><b>25</b><i>Dec</i></div><div><h3>Lorem ipsum dolor sit amet,</h3><div class="time">◷ 11:00 PM to 7 : 00 pm</div><p>Lorem consectetur adipiscing elit.Lorem consectetur adipiscing elit.Lorem const.</p></div></div>
  <div class="post"><div class="date"><b>25</b><i>Dec</i></div><div><h3>Lorem ipsum dolor sit amet,</h3><div class="time">◷ 11:00 PM to 7 : 00 pm</div><p>Lorem consectetur adipiscing elit.Lorem consectetur adipiscing elit.Lorem const.</p></div></div>
</section>
<h2 class="abs video-title">Video</h2>
<div class="abs video" role="img" aria-label="Aerial view of a paved office parking lot"><div class="play"><svg width="10" height="10" viewBox="0 0 10 10"><path d="M2 1l7 4-7 4z" fill="#fff"/></svg></div></div>
<footer class="footer">
  <div class="abs" style="left:34px;top:1005px"><h4>Menu</h4><ul><li class="current">Home</li><li>Commercial</li><li>Residential</li><li>About Us</li><li>Free Estimate</li><li>Testimonials</li><li>Blog</li></ul></div>
  <div class="abs" style="left:199px;top:1005px"><h4>Menu</h4><ul><li>Privacy policy</li><li>Site map</li><li>Suraocuse Ny</li><li>Buffalo Ny</li><li>Rochester NY</li></ul></div>
  <div class="abs" style="left:365px;top:1005px"><h4>Newsletter</h4>
    <div class="field" style="margin-top:11px">First Name</div>
    <div class="field" style="margin-top:14px">Enter Email</div>
    <div class="send" style="margin-top:14px">Send</div></div>
  <div class="abs" style="left:630px;top:1005px"><h4>Payment</h4>
    <div class="cards"><span>Cardora</span><span>Findpay</span><span>Amberline</span><span>Vestra</span></div>
    <div class="badge" style="margin:15px 0 0 38px"></div></div>
</footer>
<div class="abs copyright">Copyright © 2014 Brontivel, All Rights Reserved.</div>
</body>
</html>
```